Wordpress Design Project (Brannock)

We need a wordpress design for an established auction and real estate company based in Minnesota. The winning design will incorporate the colors of logo (red white and black) creatively in a very professional and clean layout. Client mentions liking the site http://www.quillbrook.example/ and http://www.tarvenlodeauction.example/ as a general idea for what they like.

Industry/Entity Type

Real Estate

Requirements
Must have
• Navigation:
1) Home - will have auction list, no text
2) Upcoming Auctions
3) Online Auctions
4) Real Estate
5) Auction Gallery
6) For Sale
7) About Us
8) Contact Us

Sidebar widget will include:
- email signup
- asset for sale fader (seen in Featured Listings at http://www.tarvenlodeauction.example/)
- Slideshow - initial image attached
- Video widget (image attached)
- social media icons for Vidlark, Friendspan, Chirpel, Workloop and RSS feed
- testimonials

Footer will have smaller logo and contact info
Nice to have
• Nice to Have:
- use of drop-down menu design for 'About Us'
1) About Brannock
2) Testimonials

```html
<!DOCTYPE html>
<html lang="en">
<head>
<meta charset="utf-8">
<title>Brannock Auction &amp; Real Estate Services</title>
<link rel="stylesheet" href="https://fonts.googleapis.com/css2?family=Raleway:wght@300;400;600&family=Oswald:wght@400&family=Arimo:wght@400;700&display=swap">
<style>
:root{
  --red:#a02a30;
  --red-dark:#841d22;
  --red-light:#b8353b;
  --ink:#222;
  --bar:#3b3b3b;
  --panel:#e5e5e5;
  --panel-edge:#d4d4d4;
  --white:#fff;
}
*{box-sizing:border-box;margin:0;padding:0}
html,body{width:970px;height:1200px;overflow:hidden}
body{position:relative;background:linear-gradient(#ececec,#f7f7f7 160px,#fff 300px);font-family:"Arimo",Arial,sans-serif;color:var(--ink)}
.abs{position:absolute}

.nav{left:0;top:0;width:970px;height:33px;background:var(--red);border-bottom:3px solid var(--bar);display:flex;justify-content:center}
.nav ul{list-style:none;display:flex;align-items:center;height:30px}
.nav li{color:var(--white);font-size:10px;padding:0 23px;border-left:1px solid rgba(255,255,255,.18);line-height:16px}
.nav li:first-child{border-left:none}

.logo{left:93px;top:60px;display:flex;align-items:center;gap:8px}
.logo .mark{width:26px;height:26px;background:var(--red)}
.logo .name{font-family:"Raleway",sans-serif;font-weight:600;font-size:30px;color:var(--red)}

.social{top:69px;width:35px;height:35px;border-radius:50%}
.s1{left:403px;background:#1c4f7e}.s2{left:447px;background:#2a9fdc}.s3{left:491px;background:#f0961c}.s4{left:534px;background:#b5b5b5}
.s4 svg{display:block;margin:11px auto}

.call{left:610px;top:71px;width:265px;height:32px;border-top:1px dotted #999;border-bottom:1px dotted #999;display:flex;align-items:center;gap:6px;white-space:nowrap}
.call .ico{flex:none;width:22px;height:22px;background:var(--red);border-radius:3px;display:flex;align-items:center;justify-content:center}
.call .txt{font-family:"Oswald",sans-serif;font-size:12.5px;color:#222;line-height:1}
.call .num{font-size:17px;color:var(--red);margin-left:3px}

.signup{left:89px;top:185px;width:240px;height:247px;background:var(--red);border:3px solid #fff;border-radius:10px 0 0 10px;box-shadow:0 0 4px rgba(0,0,0,.25)}
.signup h2{position:absolute;left:70px;top:24px;font-family:"Raleway",sans-serif;font-weight:400;font-size:18px;color:#fff}
.signup .gavel{position:absolute;left:16px;top:10px}
.field{position:absolute;left:27px;width:175px;height:26px;border:1px solid #c9545a;border-radius:5px;color:#f2c9cb;font-size:11px;padding:6px 9px}
.btn-sub{position:absolute;left:114px;top:188px;width:87px;height:27px;border-radius:6px;background:linear-gradient(#c08253,#8f5530);color:#fff;font-family:"Oswald",sans-serif;font-size:14px;text-align:center;line-height:27px;letter-spacing:.5px}

.hero{left:322px;top:155px;width:562px;height:303px;background:#fff;border-radius:10px;box-shadow:0 0 4px rgba(0,0,0,.25);padding:4px}
.hero .photo{width:100%;height:100%;border-radius:7px;background:linear-gradient(135deg,#2f8a2e,#6b6d5c 45%,#3e7b33 70%,#c8c04a)}

.widget{left:92px;width:228px;background:var(--panel);border:1px solid var(--panel-edge);border-radius:5px}
.widget .head{position:relative;height:32px;background:linear-gradient(var(--red-light),var(--red-dark));border-radius:5px 5px 0 0;margin:2px 2px 0;color:#fff;font-family:"Raleway",sans-serif;font-size:20px;font-weight:400;padding:2px 15px}
.widget .head:after{content:"";position:absolute;left:20px;bottom:-7px;border:7px solid transparent;border-bottom:0;border-top-color:var(--red-dark)}
.thumb{position:absolute;border:3px solid #fff;box-shadow:0 0 2px rgba(0,0,0,.3);background:linear-gradient(135deg,#3d8a31,#6a6b60 50%,#3c7d31)}
.asset-date{position:absolute;left:15px;top:146px;font-size:10px;font-weight:700;color:var(--red)}
.asset-text{position:absolute;left:16px;top:162px;width:200px;font-size:10px;line-height:13px}
.more{position:absolute;right:18px;top:210px;font-size:9.5px;font-style:italic;color:var(--red)}
.video{position:absolute;left:9px;top:50px;width:210px;height:112px;background:linear-gradient(#d8d8d8,#f3f3f3 40%,#c13a3f 60%,#e7e7e7);border:1px solid #bbb}
.video .title{position:absolute;left:10px;top:2px;color:#fff;font-size:9.5px;font-weight:700;text-shadow:0 1px 1px #000}
.video .play{position:absolute;left:88px;top:58px;width:30px;height:30px;border-radius:50%;border:2px solid #fff;background:rgba(255,255,255,.3)}
.video .play:after{content:"";position:absolute;left:10px;top:7px;border:6px solid transparent;border-left:9px solid #fff;border-right:0}
.quote{position:absolute;left:14px;top:54px;width:200px;font-size:9.5px;line-height:13.8px;color:#444}
.quote .q{font-family:Georgia,serif;font-size:22px;color:#999;line-height:0;vertical-align:-6px}

.welcome{left:340px;top:484px;display:flex;align-items:center;gap:8px}
.welcome h1{font-family:"Raleway",sans-serif;font-weight:400;font-size:19px;color:var(--red);letter-spacing:.5px}
.welcome .brand{font-family:"Raleway",sans-serif;font-weight:600;font-size:19px;color:var(--red)}
.intro{left:340px;top:521px;width:543px;font-size:10px;line-height:12.6px}

.listing{left:338px;width:547px}
.listing .bar{height:24px;background:var(--bar);border-radius:4px 4px 0 0;color:#fff;font-size:10.5px;font-weight:700;padding:6px 11px}
.listing .body{background:var(--panel);padding:7px 11px 11px;height:212px}
.card{background:#fff;border:1px solid #d6d6d6;border-radius:3px;position:relative}
.card.top{height:102px}
.card.bottom{height:74px;margin-top:9px}
.card .pic{position:absolute;left:11px;top:10px;width:106px;height:78px;border:2px solid #fff;box-shadow:0 0 2px rgba(0,0,0,.35);background:linear-gradient(#4b5e3b,#7d8b6c 50%,#a2a698)}
.card h3{position:absolute;left:125px;top:16px;font-family:"Raleway",sans-serif;font-weight:600;font-size:14.5px;color:var(--red)}
.card .desc{position:absolute;left:125px;top:38px;width:388px;font-size:9.5px;line-height:14.5px;text-align:justify}
.btn{position:absolute;left:18px;width:83px;height:22px;border-radius:4px;color:#fff;font-size:9.5px;font-weight:700;display:flex;align-items:center;gap:8px;padding-left:11px}
.btn.details{top:8px;background:linear-gradient(#d44a4f,#9e2328)}
.btn.photos{top:40px;background:linear-gradient(#555,#1f1f1f);padding-left:10px}
.btn.details span.i{width:14px;height:8px;background:linear-gradient(90deg,#fff 45%,transparent 45%)}
.btn.photos span.i{width:12px;height:10px;border:1.5px solid #fff;border-radius:2px}
.card .live{position:absolute;left:124px;top:12px;font-size:12px;color:var(--red)}
.card .meta{position:absolute;left:124px;top:34px;font-size:9.5px;line-height:15px}

.footer{left:0;top:1127px;width:970px;height:73px;background:linear-gradient(var(--red),var(--red-dark));border-top:3px solid #5a1215;color:#fff}
.footer .info{position:absolute;left:89px;top:10px;font-size:10px;line-height:18px}
.footer .flogo{position:absolute;right:90px;top:10px;display:flex;align-items:center;gap:6px;font-family:"Raleway",sans-serif;font-weight:600;font-size:18px;color:#fff}
.footer .flogo i{width:14px;height:14px;background:#fff;display:block}
.footer .powered{position:absolute;right:90px;top:53px;font-size:10px}
</style>
</head>
<body>

<nav class="abs nav"><ul>
  <li>Home</li><li>Upcoming Auctions</li><li>Online Auctions</li><li>Real Estate</li><li>Auction Gallery</li><li>For Sale</li><li>About Us</li><li>Contact Us</li>
</ul></nav>

<div class="abs logo"><span class="mark"></span><span class="name">Brannock</span></div>

<a class="abs social s1" aria-label="Friendspan"></a>
<a class="abs social s2" aria-label="Chirpel"></a>
<a class="abs social s3" aria-label="RSS feed"></a>
<a class="abs social s4" aria-label="Email">
  <svg width="16" height="12" viewBox="0 0 16 12"><rect x="0.5" y="0.5" width="15" height="11" fill="none" stroke="#fff"/><path d="M0.5 0.5 L8 7 L15.5 0.5" fill="none" stroke="#fff"/></svg>
</a>

<div class="abs call">
  <span class="ico"><svg width="13" height="13" viewBox="0 0 24 24"><path fill="#fff" d="M6.6 10.8c1.4 2.8 3.8 5.1 6.6 6.6l2.2-2.2c.3-.3.7-.4 1-.2 1.1.4 2.3.6 3.6.6.6 0 1 .4 1 1V20c0 .6-.4 1-1 1C10.6 21 3 13.4 3 4c0-.6.4-1 1-1h3.5c.6 0 1 .4 1 1 0 1.3.2 2.5.6 3.6.1.3 0 .7-.2 1z"/></svg></span>
  <span class="txt">CALL US TOLL-FREE ON<span class="num">1800 555 019</span></span>
</div>

<section class="abs signup">
  <svg class="gavel" width="48" height="48" viewBox="0 0 48 48"><rect x="18" y="6" width="16" height="10" rx="2" transform="rotate(-30 26 11)" fill="#c08a4e"/><rect x="6" y="20" width="22" height="4" transform="rotate(-30 17 22)" fill="#c08a4e"/><rect x="10" y="40" width="26" height="5" rx="2" fill="#c08a4e"/></svg>
  <h2>EMAIL SIGN-UP</h2>
  <div class="field" style="top:63px">First Name</div>
  <div class="field" style="top:113px">Last Name</div>
  <div class="field" style="top:163px">Email Address</div>
  <div class="btn-sub" style="top:188px;left:114px">SUBSCRIBE</div>
</section>

<div class="abs hero"><div class="photo" role="img" aria-label="Slideshow photo of a crowd at a farm equipment auction among rows of tractors"></div></div>

<aside class="abs widget" style="top:480px;height:230px">
  <div class="head">Asset for sale fader</div>
  <div class="thumb" style="left:15px;top:55px;width:194px;height:77px" role="img" aria-label="Featured asset photo: tractors at auction"></div>
  <div class="asset-date">Saturday March 16, 2013 at 10:00 AM</div>
  <p class="asset-text">simply dummy text of the simply dummy text of the printing and typesetting industry printing and industry.</p>
  <div class="more">More Details &raquo;</div>
</aside>

<aside class="abs widget" style="top:732px;height:173px">
  <div class="head">Watch the Video</div>
  <div class="video" role="img" aria-label="Video still of the online bidding screen">
    <span class="title">Brannock Bidder Tutorial.mp4</span>
    <span class="play"></span>
  </div>
</aside>

<aside class="abs widget" style="top:926px;height:174px">
  <div class="head">Client Testimonials</div>
  <p class="quote"><span class="q">&ldquo;</span> Ipsum has been the industry's standard dummy text ever since the 1500s, when an unknown printer took a galley of type and scrambled it to make a type specimen book. It has survived not only five centuries of type and scrambled it to make a type specimen book. It has survived <span class="q">&rdquo;</span></p>
</aside>

<div class="abs welcome"><h1>WELCOME TO</h1><span class="brand">Brannock</span></div>
<p class="abs intro">simply dummy text of the printing and typesetting industry. Lorem Ipsum has been the industry's standard dummy text ever since the 1500s, when an unknown printer took a galley of type and scrambled it to make a type specimen book. It has survived not only five centuries, but also the leap into electronic typesetting, remaining essentially unchanged. It was popularised in the 1960s.</p>

<section class="abs listing" style="top:591px">
  <div class="bar">VEHICLES * TRACTORS * FARM MACHINERY</div>
  <div class="body">
    <div class="card top">
      <div class="pic" role="img" aria-label="Photo of a white sedan parked on grass"></div>
      <h3>FURNITURE * ANTIQUES * COLLECTIBLES</h3>
      <p class="desc"><b>HOUSE TRACT: 1 ½ Story frame home located on a 3.5 acre lot.</b> SMALL FARM TRACTS: Two tracts of 30.97 acres and 39.66 acres. BUILDING SITES: Two tracts of approximately five acres each with good frontage on Millstone Road.</p>
    </div>
    <div class="card bottom">
      <div class="btn details"><span class="i"></span>Details</div>
      <div class="btn photos"><span class="i"></span>Photos</div>
      <div class="live">Live On-Site Auction</div>
      <div class="meta">Begins:&nbsp; Saturday, June 08, 2013 at 10:00 AM EDT<br>Location: 2210 Millstone Road&nbsp; Dunmore, MN 56012</div>
    </div>
  </div>
</section>

<section class="abs listing" style="top:864px">
  <div class="bar">VEHICLES * TRACTORS * FARM MACHINERY</div>
  <div class="body">
    <div class="card top">
      <div class="pic" role="img" aria-label="Photo of a white sedan parked on grass"></div>
      <h3>FURNITURE * ANTIQUES * COLLECTIBLES</h3>
      <p class="desc"><b>HOUSE TRACT: 1 ½ Story frame home located on a 3.5 acre lot.</b> SMALL FARM TRACTS: Two tracts of 30.97 acres and 39.66 acres. BUILDING SITES: Two tracts of approximately five acres each with good frontage on Millstone Road.</p>
    </div>
    <div class="card bottom">
      <div class="btn details"><span class="i"></span>Details</div>
      <div class="btn photos"><span class="i"></span>Photos</div>
      <div class="live">Live On-Site Auction</div>
      <div class="meta">Begins:&nbsp; Saturday, June 08, 2013 at 10:00 AM EDT<br>Location: 2210 Millstone Road&nbsp; Dunmore, MN 56012</div>
    </div>
  </div>
</section>

<footer class="abs footer">
  <div class="info"><b>BRANNOCK</b> Auctions<br>48 Elmwood Avenue NE &bull; Larkfield, MN 56301<br>P: 320-555-0187 &bull; F: 320-555-0189 &bull; info@brannockauction.example</div>
  <div class="flogo"><i></i>Brannock</div>
  <div class="powered">Powered by: BidHallway.example and GavelRegistry.example</div>
</footer>

</body>
</html>
```